New Service Brochure for The Brackenford Spa

Hi All! We are looking for a new brochure design- tri-fold, double sided, and full color. We are a certified Tovrel Spa for men and women in the heart of the Catskill Mountains of upstate New York. Our clients would describe us as laid back luxury with no pretensions and a home away from home vibe. Our font is Avalon. Key colors are black, white and gold. Looking for an inviting, clean, and modern/minimalist spread with a touch of elegance. No orchid imagery, please. I would like our "Tovrel Spa" logo on cover, too please. Front cover image with with logo and "Tovrel Spa" Sticker . Bottom of back with contact info. We would prefer massages go on left inside page, facials in middle and right inside, nails on back left, but we are open to new or different layout proposals. Thank you!

Target Market(s)

Men & Women.

Industry/Entity Type

Health And Wellness

Font styles to use
Other font styles liked:
• Avalon is our signature font

Requirements
Must have
• Easy on the eyes.
Nice to have
• Negative space.
Should not have
• No orchids. Busy lines and wild colors.

```html
<!DOCTYPE html>
<html lang="en">
<head>
<meta charset="utf-8">
<title>The Brackenford Spa – Tri-fold Brochure, Outside</title>
<link rel="stylesheet" href="https://fonts.googleapis.com/css2?family=Didact+Gothic&family=Montserrat:ital,wght@0,700;1,700&display=swap">
<style>
  :root {
    --gold: #d9ab35;
    --gold-deep: #c8951f;
    --black: #0c0406;
    --white: #ffffff;
    --backdrop: #9c9c9c;
    --plum: #5b3c6e;
    --plum-dark: #2d1a2e;
    --lilac: #b9a6d6;
    --wood: #6f5a4a;
    --clay: #a35a2c;
    --leaf: #5c9a3a;
    --sans: "Didact Gothic", "Century Gothic", sans-serif;
    --head: "Montserrat", "Century Gothic", sans-serif;
  }
  * { margin: 0; padding: 0; box-sizing: border-box; }
  html, body { width: 1200px; height: 800px; overflow: hidden; }
  body { background: var(--backdrop); font-family: var(--sans); color: var(--black); }

  .brochure {
    position: absolute; left: 60px; top: 30px;
    width: 1080px; height: 740px;
    display: flex;
    box-shadow: 0 6px 18px rgba(0,0,0,.25);
  }
  .panel { position: relative; width: 360px; height: 740px; overflow: hidden; }
  .panel-bg { position: absolute; inset: 0; width: 360px; height: 740px; }

  /* ---- Nails menu panel ---- */
  .menu { position: absolute; left: 26px; top: 28px; width: 308px; }
  .menu-title { font-family: var(--head); font-style: italic; font-weight: 700; font-size: 13px; margin-bottom: 5px; }
  .menu-intro { font-size: 8.6px; line-height: 1.3; font-style: italic; margin-bottom: 9px; }
  .service { margin-bottom: 8px; }
  .service-head { display: flex; justify-content: space-between; font-family: var(--head); font-style: italic; font-weight: 700; font-size: 10px; margin-bottom: 2px; }
  .service-desc { font-size: 8.4px; line-height: 1.28; font-style: italic; }

  /* ---- Contact panel ---- */
  .contact { position: absolute; left: 0; top: 44px; width: 360px; text-align: center; color: var(--white); }
  .section-title { font-family: var(--head); font-weight: 700; font-size: 20px; letter-spacing: .5px; }
  .rule { width: 210px; height: 1.5px; background: currentColor; margin: 10px auto 14px; }
  .contact-lead { font-size: 12.5px; line-height: 1.35; margin-bottom: 26px; }
  .contact-item { margin-bottom: 14px; font-size: 14px; line-height: 1.3; }
  .icon { display: block; margin: 0 auto 6px; width: 16px; height: 16px; }

  .hours { position: absolute; left: 0; top: 588px; width: 360px; text-align: center; }
  .hours .section-title { font-size: 18px; }
  .hours .rule { width: 200px; margin: 8px auto 10px; }
  .hours-list { font-size: 19px; line-height: 1.25; }
  .follow { margin-top: 10px; font-size: 13px; display: flex; justify-content: center; align-items: center; gap: 9px; }
  .social-dot { width: 13px; height: 13px; border-radius: 50%; background: var(--black); }

  /* ---- Cover panel ---- */
  .brand { position: absolute; left: 40px; top: 40px; width: 290px; text-align: center; }
  .brand-name { font-size: 34px; line-height: 1.02; letter-spacing: 1px; }
  .brand-tag { margin-top: 10px; font-size: 13px; }
  .cover-badge { position: absolute; right: 40px; top: 520px; width: 62px; height: 62px; border-radius: 50%; background: radial-gradient(circle at 40% 35%, #8cc35a, var(--leaf)); border: 3px solid #e8f3dc; }
  .tagline { position: absolute; left: 0; top: 612px; width: 360px; text-align: center; color: var(--white); }
  .tagline-main { font-family: var(--head); font-weight: 700; font-size: 20px; letter-spacing: .5px; }
  .tagline-sub { font-size: 19px; letter-spacing: 1px; margin-top: 2px; }
  .web-pill { display: inline-block; margin-top: 14px; padding: 5px 22px; border-radius: 16px; background: linear-gradient(90deg, var(--gold-deep), var(--gold)); color: var(--black); font-size: 14px; font-weight: 700; font-family: var(--sans); }
</style>
</head>
<body>
<main class="brochure">

  <!-- Back left: nails -->
  <section class="panel panel-nails">
    <svg class="panel-bg" viewBox="0 0 360 740">
      <defs>
        <linearGradient id="footBath" x1="0" y1="0" x2="1" y2="1">
          <stop offset="0" stop-color="#8a7766"/>
          <stop offset=".5" stop-color="#a35a2c"/>
          <stop offset="1" stop-color="#6f5a4a"/>
        </linearGradient>
      </defs>
      <rect width="360" height="740" fill="url(#footBath)" role="img" aria-label="Photo of feet soaking in a bowl with petals and stones beside spa herbs"/>
      <path d="M0 0 H360 V556 C290 610 170 622 92 590 C48 570 18 532 0 488 Z" fill="var(--white)"/>
      <path d="M0 0 H360 V544 C290 598 170 610 95 578 C50 558 20 520 0 476 Z" fill="var(--gold)"/>
    </svg>
    <div class="menu">
      <h2 class="menu-title">HANDS &amp; FEET:</h2>
      <p class="menu-intro">Sink into a pedicure throne in our nail lounge. Our soaks and scrubs are blended in house from fresh, natural and organic ingredients. Every nail service includes nail and cuticle care, massage and a polish of your choice.</p>
      <div class="service"><div class="service-head"><span>Mountain Herb Manicure</span><span>$65</span></div><p class="service-desc">Hydrate, smooth and clarify tired hands. Gentle cleansing oil, herbal exfoliant and a soothing hand treatment. 55 minutes.</p></div>
      <div class="service"><div class="service-head"><span>Hot Stone Manicure</span><span>$65</span></div><p class="service-desc">Melt tension and stress with a warm stone hand and arm massage. Soothe and soften tired hands with herbal mitts. 55 minutes.</p></div>
      <div class="service"><div class="service-head"><span>Renewal Manicure</span><span>$75</span></div><p class="service-desc">A full renewal for hands. Smoothing lava scrub, brightening masque and rich firming hand creme. 55 minutes.</p></div>
      <div class="service"><div class="service-head"><span>Brackenford Spa Pedicure</span><span>$75</span></div><p class="service-desc">A classic pedicure with a calming mud mask, paraffin wrap and a reviving foot and calf massage, topped with polish. 55 minutes.</p></div>
      <div class="service"><div class="service-head"><span>Alder Brook Pedicure</span><span>$85</span></div><p class="service-desc">Softens calluses and relieves tired feet. Spring cleaning and perfectly polished toes. Soak, scrub, cuticle and nail care, hot stone leg massage. 55 minutes.</p></div>
      <div class="service"><div class="service-head"><span>Spring Citrus Pedicure</span><span>$45</span></div><p class="service-desc">Sunny spring days meet April showers. Refreshing yet grounding, a bright pick me up. Soak, scrub, cuticle and nail care, polish. 30 minutes.</p></div>
    </div>
  </section>

  <!-- Back middle: contact & hours -->
  <section class="panel panel-contact">
    <svg class="panel-bg" viewBox="0 0 360 740" aria-hidden="true">
      <rect width="360" height="740" fill="var(--black)"/>
      <path d="M0 544 C120 520 270 530 360 640 V740 H0 Z" fill="var(--white)"/>
      <path d="M0 556 C120 532 262 546 350 650 L360 662 V740 H0 Z" fill="var(--gold)"/>
    </svg>
    <div class="contact">
      <h2 class="section-title">GET IN TOUCH</h2>
      <div class="rule"></div>
      <p class="contact-lead">To Book An Appointment, Or For Any<br>Questions, Call Us Or Send Us A Message.</p>
      <p class="contact-item">
        <svg class="icon" viewBox="0 0 16 16"><circle cx="8" cy="8" r="8" fill="#fff"/><path d="M5 4.5 L6.6 4.2 L7.3 6 L6.4 6.8 C6.9 7.9 7.8 8.9 9 9.5 L9.8 8.6 L11.6 9.3 L11.4 11 C8 11 5 8 5 4.5Z" fill="#0c0406"/></svg>
        (555) 014-2286
      </p>
      <p class="contact-item">
        <svg class="icon" viewBox="0 0 16 16"><circle cx="8" cy="8" r="8" fill="#fff"/><rect x="4" y="5" width="8" height="6" fill="#0c0406"/><path d="M4 5 L8 8.4 L12 5" stroke="#fff" stroke-width=".9" fill="none"/></svg>
        info@thebrackenfordspa.com
      </p>
      <p class="contact-item">
        <svg class="icon" viewBox="0 0 16 16"><circle cx="8" cy="8" r="8" fill="#fff"/><path d="M8 12.5 C6 10 5 8.4 5 7 A3 3 0 0 1 11 7 C11 8.4 10 10 8 12.5Z" fill="#0c0406"/><circle cx="8" cy="7" r="1.1" fill="#fff"/></svg>
        42 Alder Brook Road Brackenford,<br>NY 12999 Just off Main Street!
      </p>
      <p class="contact-item">
        <svg class="icon" viewBox="0 0 16 16"><circle cx="8" cy="8" r="8" fill="#fff"/><circle cx="8" cy="8" r="4" fill="none" stroke="#0c0406" stroke-width="1"/><path d="M4 8 H12 M8 4 V12" stroke="#0c0406" stroke-width=".8"/></svg>
        www.thebrackenfordspa.com
      </p>
    </div>
    <div class="hours">
      <h2 class="section-title">SPRING HOURS</h2>
      <div class="rule"></div>
      <p class="hours-list">Thurs-Sat: 10am-6pm<br>Sun-Mon: 10am-5pm<br>Tues &amp; Wed: Closed</p>
      <div class="follow"><span>Follow Us-</span><span class="social-dot"></span><span class="social-dot"></span><span class="social-dot"></span></div>
    </div>
  </section>

  <!-- Front cover -->
  <section class="panel panel-cover">
    <svg class="panel-bg" viewBox="0 0 360 740">
      <defs>
        <linearGradient id="candleScene" x1="0" y1="0" x2="1" y2="1">
          <stop offset="0" stop-color="#b9a6d6"/>
          <stop offset=".45" stop-color="#5b3c6e"/>
          <stop offset="1" stop-color="#2d1a2e"/>
        </linearGradient>
      </defs>
      <rect width="360" height="740" fill="var(--black)"/>
      <path d="M0 380 C80 540 220 600 360 600 V612 C210 616 70 560 0 400 Z" fill="var(--white)"/>
      <path d="M0 110 C70 205 220 228 360 262 V600 C220 600 80 540 0 380 Z" fill="url(#candleScene)" role="img" aria-label="Photo of lit candles, a rolled towel, shells and spa stones"/>
      <path d="M0 0 H360 V276 C220 242 60 222 0 124 Z" fill="var(--white)"/>
      <path d="M0 0 H360 V262 C220 228 70 205 0 110 Z" fill="var(--gold)"/>
    </svg>
    <div class="brand">
      <h1 class="brand-name">The Brackenford<br>Spa</h1>
      <p class="brand-tag">a boutique spa for Men &amp; Women</p>
    </div>
    <div class="cover-badge" role="img" aria-label="Certified spa badge"></div>
    <div class="tagline">
      <p class="tagline-main">ESCAPE THE CONGESTION</p>
      <p class="tagline-sub">OF EVERYDAY LIFE</p>
      <span class="web-pill">www.thebrackenfordspa.com</span>
    </div>
  </section>

</main>
</body>
</html>
```